This is a label for a new sake made in Japan imported into Aust

This will be a bottle label for a new sake imported into Australia. The hero of the label is the Velmora. We have joined the "O" meaning great in Japanese and used sake with "Z" to have Velmora with the play on words using Oz as in our slang for Aussie. A modern label with a Japanese take is key. This is a premium sake made in Japan for the Australian market.
The "Tall Casks" up the top is the name of the company, we have yet to design a logo for the company.

Target Market(s)

Alcohol

Logo Text

Velmora

Font styles to use
Serif

Requirements
Must have
• easy to read, with a hint of Japanese origin
Should not have
• too busy

```html
<!DOCTYPE html>
<html lang="en">
<head>
<meta charset="utf-8">
<title>Velmora – Premium Japanese Sake Label</title>
<link href="https://fonts.googleapis.com/css2?family=Crimson+Pro:ital,wght@0,500;1,400&display=swap" rel="stylesheet">
<style>
  :root {
    --blush: #f9eef1;
    --blush-warm: #f9ebe6;
    --ink: #000000;
    --sake-red: #b52225;
    --paper-white: #ffffff;
    --gold-1: #f6d36b;
    --gold-2: #d9a845;
    --gold-3: #f4f3ae;
    --gold-4: #b38233;
  }
  * { margin: 0; padding: 0; box-sizing: border-box; }
  html, body { width: 1200px; height: 1200px; overflow: hidden; background: var(--blush); }
  .label {
    position: relative;
    width: 1200px;
    height: 1200px;
    background: var(--blush);
    overflow: hidden;
  }
  .petal-field {
    position: absolute;
    inset: 0;
    background: linear-gradient(160deg, var(--blush-warm) 0%, var(--blush) 45%, var(--blush) 60%, var(--blush-warm) 100%);
  }
  .gold-trim { position: absolute; inset: 0; }
  .company-name {
    position: absolute;
    top: 22px;
    left: 0;
    width: 1200px;
    text-align: center;
    font-family: "Crimson Pro", serif;
    font-style: italic;
    font-size: 68px;
    line-height: 1;
    color: var(--ink);
  }
  .wordmark {
    position: absolute;
    top: 385px;
    left: 10px;
    width: 1200px;
    text-align: center;
    font-family: "Crimson Pro", serif;
    font-weight: 500;
    font-size: 275px;
    line-height: 1;
    color: var(--ink);
  }
  .tagline {
    position: absolute;
    left: 604px;
    top: 872px;
    width: 596px;
    height: 75px;
    background: var(--sake-red);
    display: flex;
    align-items: center;
    justify-content: center;
    font-family: "Crimson Pro", serif;
    font-style: italic;
    font-size: 62px;
    line-height: 1;
    color: var(--paper-white);
  }
</style>
</head>
<body>
<main class="label">
  <div class="petal-field" role="img" aria-label="Soft scattered cherry blossom petals across the label background"></div>

  <svg class="gold-trim" width="1200" height="1200" viewBox="0 0 1200 1200" aria-hidden="true">
    <defs>
      <linearGradient id="gold" x1="0" y1="0" x2="1" y2="0">
        <stop offset="0" stop-color="var(--gold-1)"/>
        <stop offset="0.3" stop-color="var(--gold-2)"/>
        <stop offset="0.58" stop-color="var(--gold-3)"/>
        <stop offset="1" stop-color="var(--gold-4)"/>
      </linearGradient>
    </defs>
    <path class="top-band" fill="url(#gold)"
      d="M0 0 H1200 V42 H840 C800 42 770 70 740 95 C690 130 630 140 590 140 C540 140 480 130 440 100 C400 72 380 42 330 40 C200 38 100 42 0 42 Z"/>
    <rect class="bottom-band" x="0" y="1164" width="1200" height="36" fill="url(#gold)"/>
  </svg>

  <p class="company-name">Tall Casks</p>
  <h1 class="wordmark">Velmora</h1>
  <p class="tagline">Premium Japanese Sake</p>
</main>
</body>
</html>
```